Business Card for Ferncliff Massage

I need a business card for my massage therapy & cannabis oil practice. I already have a logo,the "massage" got edited out of this file. I will send the original soon. I need these elements to be on the card:
web: FerncliffMassage.example
ph: 541/382-9147
email: Marla.Quintavelle@mailbox.example
Other slogans, statements to consider:
Science Geek, Massage Therapist, Neuromuscular Therapy, Cannabis Spa Treatments, Raindrop Therapy, Essential Oils
Target Market(s)
women between 20 & 65, people with enough $ to afford regular massage, people who recently had a motor vehicle accident, Halvora HMC insured
Industry/Entity Type
Massage Therapy
Contact Information for Business Card
I would like to see my bear logo featured; contact details, greens & blues preferred colors.

```html
<!DOCTYPE html>
<html lang="en">
<head>
<meta charset="utf-8">
<title>Ferncliff Massage – Business Card</title>
<link rel="stylesheet" href="https://fonts.googleapis.com/css2?family=Crimson+Text:wght@400;600;700&display=swap">
<style>
  :root {
    --canvas: #e4e4e6;
    --card-white: #ffffff;
    --taupe: #a08e82;
    --taupe-light: #b3a59b;
    --taupe-dark: #6f655c;
    --back-top: #857669;
    --back-bottom: #ab9d93;
    --fern-green: #3f7f3b;
    --ink: #5c4f45;
    --ink-soft: #8c7a6d;
    --on-dark: #f7f3ef;
  }
  * { box-sizing: border-box; margin: 0; padding: 0; }
  html, body { width: 1200px; height: 800px; overflow: hidden; }
  body {
    background: var(--canvas);
    font-family: "Crimson Text", Georgia, serif;
    position: relative;
  }
  .card {
    position: absolute;
    top: 252px;
    width: 520px;
    height: 296px;
    overflow: hidden;
    box-shadow: 0 6px 18px rgba(0,0,0,0.12);
  }
  .card--front { left: 50px; background: var(--card-white); }
  .card--back {
    left: 630px;
    background: linear-gradient(160deg, var(--back-top), var(--back-bottom));
  }
  .front-waves { position: absolute; inset: 0; }

  .brand {
    position: absolute;
    left: 34px;
    top: 96px;
    display: flex;
    align-items: center;
    gap: 12px;
  }
  .brand__dot {
    width: 26px; height: 26px;
    border-radius: 50%;
    background: var(--taupe);
  }
  .brand__name {
    font-size: 46px;
    font-weight: 400;
    color: var(--fern-green);
    line-height: 1;
    letter-spacing: 0.5px;
  }

  .contact {
    position: absolute;
    left: 262px;
    top: 62px;
    color: var(--ink);
  }
  .contact__name {
    font-size: 21px;
    font-weight: 700;
    letter-spacing: 2px;
    text-transform: uppercase;
    line-height: 1;
  }
  .contact__role {
    font-size: 14px;
    color: var(--ink-soft);
    letter-spacing: 1px;
    margin-top: 3px;
    margin-bottom: 12px;
  }
  .contact__line {
    display: flex;
    align-items: center;
    gap: 7px;
    font-size: 14px;
    font-weight: 600;
    line-height: 1.45;
  }
  .contact__icon { width: 11px; height: 11px; flex: none; fill: var(--ink-soft); }
  .contact__address {
    margin-top: 8px;
    font-size: 14px;
    font-weight: 600;
    line-height: 1.35;
  }

  .services {
    position: absolute;
    left: 54px;
    top: 40px;
    list-style: none;
    color: var(--on-dark);
    font-size: 19px;
    line-height: 1.42;
  }
  .services li { display: flex; align-items: center; gap: 14px; }
  .services li::before {
    content: "";
    width: 9px; height: 9px;
    border-radius: 50%;
    background: var(--on-dark);
  }
</style>
</head>
<body>

<section class="card card--front" aria-label="Business card front">
  <svg class="front-waves" viewBox="0 0 520 296" preserveAspectRatio="none" aria-hidden="true">
    <path d="M0 150 C120 140 230 200 300 250 C340 278 380 290 420 296 L0 296 Z" fill="var(--taupe)"/>
    <path d="M0 168 C110 160 210 210 290 262 C320 282 350 292 380 296 L0 296 Z" fill="var(--card-white)"/>
    <path d="M0 186 C100 178 190 226 270 272 C290 284 305 292 320 296 L0 296 Z" fill="var(--taupe)"/>
    <path d="M60 296 C200 296 330 276 520 220 L520 296 Z" fill="var(--taupe-dark)"/>
    <path d="M40 296 C190 296 320 284 520 244 L520 296 Z" fill="var(--card-white)"/>
    <path d="M0 296 C170 296 310 290 520 262 L520 296 Z" fill="var(--taupe-light)"/>
  </svg>

  <div class="brand">
    <span class="brand__dot"></span>
    <span class="brand__name">Ferncliff</span>
  </div>

  <div class="contact">
    <h1 class="contact__name">Dane Holloway</h1>
    <p class="contact__role">Project Manager</p>
    <p class="contact__line">
      <svg class="contact__icon" viewBox="0 0 12 12"><path d="M2.5 0.5l2 2.5-1 1.2c.6 1.4 1.8 2.6 3.3 3.3l1.2-1 2.5 2-1.2 2.2C5 11.7 0.3 7 .3 1.7z"/></svg>
      541/382-9147
    </p>
    <p class="contact__line">
      <svg class="contact__icon" viewBox="0 0 12 12"><path d="M0 2h12v8H0z M1 3l5 3.5L11 3" /></svg>
      Marla.Quintavelle@mailbox.example
    </p>
    <p class="contact__line">
      <svg class="contact__icon" viewBox="0 0 12 12"><circle cx="6" cy="6" r="5.5"/><path d="M0.5 6h11M6 .5v11" stroke="#fff" stroke-width="0.8"/></svg>
      www.FerncliffMassage.example
    </p>
    <p class="contact__address">8/41 Tamsin Ave<br>Orchard Vale QLD 4172</p>
  </div>
</section>

<section class="card card--back" aria-label="Business card back">
  <ul class="services">
    <li>Science Geek</li>
    <li>Massage Therapist</li>
    <li>Neuromuscular Therapy</li>
    <li>Cannabis Spa Treatments</li>
    <li>Raindrop Therapy</li>
    <li>Essential Oils</li>
  </ul>
</section>

</body>
</html>
```